New business! Essential Oils Label for 10 mL Essential Oils Bottles

I need a label design for my new essential oils business. The design should be easily transferable between products. Content should include:
label size W x H 1.25 x 2.875

LAVENDER
Lavandula angustifolia
VOLMIRAâ„¢
100% PURE ESSENTIAL OIL
Net 10 mL
For promotions and additional product information visit fb.com/VolmiraOils
VolmiraOils.com
Boca Raton, FL 33871
888-555-KIPO (5476)
Indications: Massage (10 drops of carrier oil for every drop of essential oil), Bath (10 drops of essential oil) or Inhalation (2-4 drops essential of on a tissue).
EXTERNAL USE ONLY- DILUTE BEFORE APPLICATION
Caution: Do not ingest the oil. Sensitive skin may be irritated by topical use. Avoid contact with eyes. Consult your healthcare practitioner before use. Store oil away from children and pets. Not meant for use during pregnancy. Seek medical care immediately if adverse reaction is experienced.

Target Market(s)

ONLINE SHOPPERS

Industry/Entity Type

Business

Font styles to use
Serif
Sans Serif

Colors

Designer to choose colors to be used in the design.

Requirements
Must have
• CONTENT AS LISTED IN PROJECT DESCRIPTION, LOGO (ATTACHED)
Nice to have
• Files with easily transferable content so the same label design can be used for multiple products.
Should not have
• Too small of print, difficult to read

```html
<!DOCTYPE html>
<html lang="en">
<head>
<meta charset="utf-8">
<title>Volmira Lavender Essential Oil Label</title>
<link rel="stylesheet" href="https://fonts.googleapis.com/css2?family=Fira+Sans:wght@300;400;600&display=swap">
<style>
  :root {
    --stage: #2b2b2b;
    --label-dark: #141414;
    --label-mid: #2a2a2a;
    --plum: #7e1a72;
    --plum-deep: #5c1254;
    --lilac-text: #e2d4ec;
    --soft-white: #e6e6e6;
    --lavender-light: #b7a8e6;
    --lavender-deep: #8d72c8;
  }
  html, body {
    margin: 0;
    padding: 0;
    width: 1134px;
    height: 1200px;
    overflow: hidden;
    background: var(--stage);
  }
  .label {
    position: absolute;
    left: 302px;
    top: 51px;
    width: 529px;
    height: 1097px;
    background: linear-gradient(160deg, var(--label-mid) 0%, var(--label-dark) 60%);
    overflow: hidden;
    font-family: "Fira Sans", sans-serif;
  }
  .label__wave-art {
    position: absolute;
    inset: 0;
    background: linear-gradient(200deg,
      rgba(126, 26, 114, 0) 0%,
      rgba(126, 26, 114, 0) 42%,
      rgba(92, 18, 84, 0.55) 62%,
      var(--plum) 80%,
      var(--plum) 100%);
  }
  .label__sprigs {
    position: absolute;
    left: 0;
    right: 0;
    bottom: 0;
    height: 170px;
    background: linear-gradient(180deg, rgba(183,168,230,0) 0%, var(--lavender-light) 35%, var(--lavender-deep) 100%);
    opacity: 0.85;
  }
  .label__text {
    position: absolute;
    left: 0;
    width: 100%;
    margin: 0;
    text-align: center;
    line-height: 1.1;
  }
  .brand {
    top: 70px;
    font-weight: 300;
    font-size: 60px;
    letter-spacing: 4px;
    color: var(--soft-white);
  }
  .brand__mark {
    font-size: 16px;
    vertical-align: top;
    letter-spacing: 0;
  }
  .purity {
    top: 362px;
    font-weight: 600;
    font-size: 28px;
    color: var(--lilac-text);
  }
  .product-name {
    top: 468px;
    font-weight: 600;
    font-size: 86px;
    color: var(--lilac-text);
  }
  .latin-name {
    top: 570px;
    font-weight: 400;
    font-size: 29px;
    color: var(--soft-white);
  }
  .net-volume {
    top: 852px;
    font-weight: 600;
    font-size: 42px;
    color: var(--soft-white);
  }
</style>
</head>
<body>
  <main class="label">
    <div class="label__wave-art" role="img" aria-label="Decorative flowing plum wave graphic sweeping across the lower label"></div>
    <div class="label__sprigs" role="img" aria-label="Illustration of lavender flower sprigs along the bottom edge"></div>

    <p class="label__text brand">VOLMIRA<span class="brand__mark">™</span></p>
    <p class="label__text purity">100% PURE ESSENTIAL OIL</p>
    <h1 class="label__text product-name">LAVENDER</h1>
    <p class="label__text latin-name">Lavandula angustifolia</p>
    <p class="label__text net-volume">Net 10 mL</p>
  </main>
</body>
</html>
```